Harrowgate Vitality Circle needs a stand-up Banner Deadline Oct 2

We need a stand-up banner design for Harrowgate University Vitality Circle. Our aim is to spread awareness of emerging ideas and technologies in various scientific fields with a particular emphasis on geroscience (hence the name), but not restricted to it. We organise various projects, talks by prominent scientists and conferences.

We urgently need a design for a vertical roll up banner to be used in our events (beside the stage) and an upcoming freshers' fair.

I'm attaching our logo (you can separate the circular logo from the "Vitality Circle" text if you like) and a picture of Cambridge that you could use if needed. We are open to use of stock photos.

Size: 800 x 2000

Target Market(s)

Harrowgate University Students

Industry/Entity Type

University

Requirements
Must have
• -Logo
• -Either "Vitality Circle" or "Harrowgate University Vitality Circle" name
• -Text "Spreading awareness of emerging ideas and technologies"
• -Circlebook page https://www.facebook.com/HarUVCirc/
• -Email huvitality@mailnest.example
Nice to have
• -Some of the colours I envision for the banner are: green, blue, white
• -Scientific and/or innovative feeling

```html
<!DOCTYPE html>
<html lang="en">
<head>
<meta charset="utf-8">
<title>Vitality Circle – Roll-up Banner</title>
<link rel="stylesheet" href="https://fonts.googleapis.com/css2?family=Open+Sans:wght@400;600;700;800&display=swap">
<style>
  :root {
    --bg: #e4e4e4;
    --white: #ffffff;
    --ink: #111111;
    --green: #23924b;
    --green-light: #8cc63f;
    --blue: #1565c0;
    --stone: #c9a866;
    --lawn: #4f8a2e;
  }
  * { margin: 0; padding: 0; box-sizing: border-box; }
  html, body {
    width: 1200px; height: 1200px; overflow: hidden;
    background: var(--bg);
    font-family: "Open Sans", Arial, sans-serif;
  }
  .banner {
    position: absolute;
    left: 365px; top: 12px;
    width: 470px; height: 1175px;
    background: var(--white);
    overflow: hidden;
    box-shadow: 0 4px 18px rgba(0,0,0,0.12);
  }
  .banner-shapes {
    position: absolute; inset: 0;
    width: 100%; height: 100%;
  }
  .brand {
    position: absolute;
    left: 48px; top: 88px;
    display: flex; align-items: center; gap: 16px;
  }
  .brand-dot {
    width: 52px; height: 52px; border-radius: 50%;
    background: var(--green);
  }
  .brand-name {
    font-weight: 600;
    font-size: 30px;
    letter-spacing: 3px;
    text-transform: uppercase;
    color: var(--green);
  }
  .headline {
    position: absolute;
    right: 50px; top: 182px;
    text-align: right;
    line-height: 1;
  }
  .headline span { display: block; }
  .headline .lead {
    font-weight: 700; font-size: 44px; color: var(--ink);
    letter-spacing: -0.5px; margin-bottom: 6px;
  }
  .headline .big {
    font-weight: 800; font-size: 62px; color: var(--green);
    margin-top: 6px; letter-spacing: 0.5px;
  }
  .headline .mid {
    font-weight: 800; font-size: 38px; color: var(--green);
    margin-top: 10px;
  }
  .headline .mid .plain { display: inline; font-weight: 400; color: var(--ink); }
  .headline .end {
    font-weight: 800; font-size: 42px; color: var(--green);
    margin-top: 8px;
  }
  .contact {
    position: absolute;
    left: 44px; top: 1016px;
    color: var(--white);
  }
  .contact .label { font-size: 18px; font-weight: 400; display: block; }
  .contact .link-web { font-size: 20px; font-weight: 700; display: block; margin-top: 6px; }
  .contact .link-mail { font-size: 24px; font-weight: 700; display: block; margin-top: 2px; }
  .contact .gap { margin-top: 20px; }
</style>
</head>
<body>
  <div class="banner">
    <svg class="banner-shapes" viewBox="0 0 320 800" preserveAspectRatio="none">
      <defs>
        <linearGradient id="scene-tone" x1="0" y1="0" x2="0" y2="1">
          <stop offset="0" stop-color="#6fa4dc"/>
          <stop offset="0.35" stop-color="#b9d3ea"/>
          <stop offset="0.55" stop-color="#c9a866"/>
          <stop offset="0.72" stop-color="#4f8a2e"/>
          <stop offset="1" stop-color="#7c8a5a"/>
        </linearGradient>
      </defs>
      <polygon class="band-blue" points="0,283 262,377 0,314" fill="var(--blue)"/>
      <g role="img" aria-label="Photograph of historic college buildings and a chapel beside a lawn, reflected in a river under a blue sky">
        <polygon class="photo-area" points="0,306 320,412 320,700 0,598" fill="url(#scene-tone)"/>
      </g>
      <polygon class="accent-green" points="222,382 320,352 320,402" fill="var(--green-light)"/>
      <polygon class="accent-green-low" points="0,602 105,640 0,636" fill="var(--green-light)"/>
      <polygon class="footer-green" points="0,640 320,728 320,800 0,800" fill="var(--green)"/>
      <rect class="footer-blue" x="0" y="790" width="320" height="4" fill="var(--blue)"/>
    </svg>

    <div class="brand">
      <span class="brand-dot"></span>
      <span class="brand-name">Vitality Circle</span>
    </div>

    <h1 class="headline">
      <span class="lead">spreading</span>
      <span class="lead">awareness of</span>
      <span class="big">EMERGING</span>
      <span class="mid">IDEAS <span class="plain">AND</span></span>
      <span class="end">TECHNOLOGIES</span>
    </h1>

    <div class="contact">
      <span class="label">Follow us on Circlebook</span>
      <span class="link-web">www.circlebook.example/HarUVCirc/</span>
      <span class="label gap">Mail us for any query</span>
      <span class="link-mail">huvitality@mailnest.example</span>
    </div>
  </div>
</body>
</html>
```